Automotive component supplier needs a business card design

We need a business card design for our company called Velmar Global Components Ltd based in the UK. We are a supplier of interior and exterior components to premium car manufacturers such as Corvane Hale, Durrant Fyfe, Maxtorn and Valdessimo. We would like to see a modern business card design that uses the colour blue.

Target Market(s)

Premium automotive car manufacturers.

Industry/Entity Type

Automotive

Contact Information for Business Card

Company Name : Velmar Global Components Limited
Address: 17 Tamsey Yard, Upper Drisk, Warwick, CV31 8RJ, United Kingdom
Web Address : www.velmarparts-example.co.uk

Font styles to use
Other font styles liked:
• Helvetica

Colors
3176b5
0255a3
85acd3
cfdeed
cee9f5
85cae6
34a6d7
0692cd
9bcb3c

Requirements
Must have
• Clear company logo and a mixture of blue colours.
Nice to have
• A high quality modern image.
Should not have
• Multiple colours.

```html
<!DOCTYPE html>
<html lang="en">
<head>
<meta charset="utf-8">
<title>Velmar Global Components – Business Card</title>
<link href="https://fonts.googleapis.com/css2?family=Arimo:wght@400;700&display=swap" rel="stylesheet">
<style>
  :root {
    --page: #e9eaec;
    --card-white: #f7f8f8;
    --slate: #3a4650;
    --slate-light: #4a5863;
    --lime: #9bcb3c;
    --lime-light: #b6dc5c;
    --blue: #0692cd;
    --ink: #3b4248;
    --ink-soft: #6b7278;
    --text-on-dark: #eef1f3;
  }
  * { box-sizing: border-box; margin: 0; padding: 0; }
  html, body { width: 1200px; height: 879px; overflow: hidden; }
  body {
    background: var(--page);
    font-family: "Arimo", Helvetica, Arial, sans-serif;
    position: relative;
  }
  .card {
    position: absolute;
    width: 520px;
    height: 298px;
    top: 290px;
    overflow: hidden;
    box-shadow: 0 6px 18px rgba(0,0,0,.18);
  }

  /* Front */
  .card-front { left: 50px; background: var(--card-white); }
  .front-topband {
    position: absolute; left: 0; top: 0; width: 100%; height: 20px;
    background: var(--slate);
  }
  .front-topband::before {
    content: ""; position: absolute; left: 0; top: 0; width: 54%; height: 100%;
    background: var(--card-white);
  }
  .front-sidepanel {
    position: absolute; right: 0; top: 20px; width: 46%; bottom: 0;
    background: linear-gradient(180deg, var(--slate-light), var(--slate));
  }
  .name-box {
    position: absolute; right: 30px; top: 20px; left: 54%; height: 150px;
    background: radial-gradient(circle at 40% 40%, var(--lime-light), var(--lime));
    border-left: 6px solid var(--card-white);
    display: flex; flex-direction: column; justify-content: center; align-items: center;
  }
  .person-name { font-weight: 700; font-size: 17px; color: var(--ink); }
  .person-role { font-size: 13px; color: var(--ink); margin-top: 3px; }
  .contact-list {
    position: absolute; left: calc(54% + 10px); top: 186px; list-style: none;
  }
  .contact-item {
    display: flex; align-items: center; gap: 10px;
    color: var(--text-on-dark); font-size: 13px; height: 26px;
  }
  .contact-icon {
    width: 16px; height: 16px; background: var(--lime);
    display: flex; align-items: center; justify-content: center;
  }
  .brand-name {
    position: absolute; left: 34px; top: 92px;
    font-size: 44px; font-weight: 700; letter-spacing: 1px;
    color: var(--blue);
  }
  .address {
    position: absolute; left: 80px; top: 168px;
    font-size: 13px; line-height: 17px; color: var(--ink-soft);
  }
  .web-bar {
    position: absolute; left: 60px; width: calc(54% - 60px); bottom: 18px; height: 26px;
    background: var(--lime);
    color: #fff; font-size: 12.5px;
    display: flex; align-items: center; padding-left: 20px;
  }
  .web-bar::after {
    content: ""; position: absolute; right: -18px; top: 0; width: 12px; height: 100%;
    background: var(--lime-light);
  }

  /* Back */
  .card-back {
    left: 630px;
    background: radial-gradient(ellipse at 45% 40%, #4d5b67, var(--slate) 70%);
  }
  .back-brand {
    position: absolute; left: 0; right: 0; top: 110px; text-align: center;
    font-size: 46px; font-weight: 700; letter-spacing: 2px; color: #f4f6f7;
  }
  .back-web {
    position: absolute; left: 0; right: 0; bottom: 36px; text-align: center;
    font-size: 12px; letter-spacing: 3px; color: #c9d0d5;
  }
  .back-web .domain { color: var(--lime); }
</style>
</head>
<body>
  <section class="card card-front" aria-label="Business card front">
    <div class="front-topband"></div>
    <div class="front-sidepanel"></div>
    <div class="name-box">
      <p class="person-name">Alan Mercer</p>
      <p class="person-role">Branch Director</p>
    </div>
    <ul class="contact-list">
      <li class="contact-item">
        <span class="contact-icon">
          <svg width="10" height="10" viewBox="0 0 10 10"><path d="M2 1l2 2-1 1c.5 1.2 1.5 2.2 2.7 2.7l1-1 2 2-1.2 1.2C4.5 9 1 5.5 1 2.2z" fill="#fff"/></svg>
        </span>+44 7700 900 412
      </li>
      <li class="contact-item">
        <span class="contact-icon">
          <svg width="10" height="10" viewBox="0 0 10 10"><rect x="2.5" y="0.5" width="5" height="9" rx="1" fill="none" stroke="#fff"/><circle cx="5" cy="7.8" r=".6" fill="#fff"/></svg>
        </span>+44 1926 555 0187
      </li>
      <li class="contact-item">
        <span class="contact-icon">
          <svg width="10" height="10" viewBox="0 0 10 10"><rect x=".5" y="2" width="9" height="6" fill="none" stroke="#fff"/><path d="M.5 2L5 5.5 9.5 2" fill="none" stroke="#fff"/></svg>
        </span>hello@velmarparts-example.co.uk
      </li>
    </ul>
    <p class="brand-name">VELMAR</p>
    <p class="address">17 Tamsey Yard, Upper Drisk<br>Warwick, CV31 8RJ<br>United Kingdom</p>
    <p class="web-bar">www.velmarparts-example.co.uk</p>
  </section>

  <section class="card card-back" aria-label="Business card back">
    <p class="back-brand">VELMAR</p>
    <p class="back-web">www.<span class="domain">velmarparts-example</span>.co.uk</p>
  </section>
</body>
</html>
```